Website for a start-up named Vlm Quarvex.

The company is currently producing a sustainable tactical training measure for soldiers in the defense industry. We’d like a simple website design. As the product hasn’t been launched yet, we will not tell too much about the product and it’s not for sale either. We have a website on wix called vlmquarvex.com which we would like to proceed with. The design just needs a professional and loving touch. We develop an add on for TK40 rifles.

Target Market(s)

Defense industry

Industry/Entity Type

Defense

Coding

Coded - Design and coding required

Number of Pages Required

1 page

```html
<!DOCTYPE html>
<html lang="en">
<head>
<meta charset="utf-8">
<title>Vlm Quarvex</title>
<link rel="stylesheet" href="https://fonts.googleapis.com/css2?family=Roboto:ital,wght@0,400;0,500;0,700;1,400;1,500;1,700&display=swap">
<style>
  :root {
    --teal: #00a596;
    --white: #ffffff;
    --text-soft: #e6e6e6;
    --page-dark: #121212;
    --band-dark: #0d0d0d;
    --mouse-grey: #6f6f6f;
  }
  * { box-sizing: border-box; margin: 0; padding: 0; }
  html, body {
    width: 1200px;
    height: 3125px;
    overflow: hidden;
    background: var(--page-dark);
    font-family: "Roboto", Arial, sans-serif;
    color: var(--white);
  }
  .page { position: relative; width: 1200px; height: 3125px; }
  .section { position: absolute; left: 0; width: 1200px; overflow: hidden; }
  .backdrop { position: absolute; inset: 0; }
  .content { position: absolute; left: 0; width: 1200px; text-align: center; }

  /* Hero: misty forest tones */
  .hero { top: 0; height: 675px; }
  .hero .backdrop {
    background:
      linear-gradient(90deg, rgba(8,8,8,0.85) 0%, rgba(10,10,10,0.55) 12%, transparent 30%, transparent 70%, rgba(10,10,10,0.6) 100%),
      linear-gradient(110deg, transparent 18%, rgba(200,200,200,0.10) 26%, transparent 32%, rgba(210,210,210,0.12) 40%, transparent 47%),
      radial-gradient(ellipse 22% 30% at 42% 30%, rgba(190,190,190,0.35), transparent 70%),
      radial-gradient(ellipse 60% 18% at 45% 92%, rgba(120,120,120,0.45), transparent 75%),
      radial-gradient(ellipse 40% 35% at 80% 20%, rgba(90,90,90,0.35), transparent 70%),
      linear-gradient(180deg, #262626 0%, #2b2b2b 35%, #1c1c1c 70%, #232323 88%, #141414 100%);
  }
  .brand-name {
    position: absolute; top: 196px; left: 0; width: 1200px;
    text-align: center; font-size: 56px; font-weight: 500;
    letter-spacing: 4px; color: var(--teal);
  }
  .hero-title { top: 332px; font-size: 24px; font-weight: 400; letter-spacing: 1.6px; }
  .hero-intro {
    top: 374px; left: 305px; width: 590px;
    font-size: 10.5px; line-height: 15px; letter-spacing: 0.6px; color: var(--text-soft);
  }
  .cta {
    position: absolute; top: 480px; left: 525px; width: 150px; height: 38px;
    background: var(--teal); color: var(--white);
    font-size: 14px; font-weight: 700; font-style: italic; letter-spacing: 1.4px;
    display: flex; align-items: center; justify-content: center; text-decoration: none;
  }

  /* Who we are: dark soldier scene tones */
  .who { top: 675px; height: 675px; }
  .who .backdrop {
    background:
      radial-gradient(ellipse 20% 25% at 78% 22%, rgba(55,80,45,0.55), transparent 75%),
      radial-gradient(ellipse 18% 20% at 92% 55%, rgba(40,55,35,0.45), transparent 75%),
      radial-gradient(ellipse 30% 28% at 22% 22%, rgba(80,80,80,0.55), transparent 75%),
      radial-gradient(ellipse 35% 22% at 45% 75%, rgba(70,70,70,0.5), transparent 75%),
      radial-gradient(ellipse 25% 18% at 85% 72%, rgba(60,60,60,0.45), transparent 75%),
      radial-gradient(ellipse 15% 25% at 8% 80%, rgba(65,65,65,0.4), transparent 75%),
      linear-gradient(180deg, #222 0%, #1d1d1d 60%, #191919 100%);
  }
  .section-heading { font-size: 22px; font-weight: 700; letter-spacing: 2px; color: var(--teal); }
  .who-heading { top: 958px; top: 283px; }
  .who-text {
    top: 325px; left: 400px; width: 400px;
    font-size: 10.5px; line-height: 15px; letter-spacing: 0.6px; color: var(--text-soft);
  }

  /* Technology: night earth tones */
  .tech { top: 1350px; height: 674px; background: var(--band-dark); }
  .tech .backdrop {
    top: 203px;
    background:
      radial-gradient(ellipse 10% 5% at 32% 65%, rgba(200,200,200,0.30), transparent 75%),
      radial-gradient(ellipse 8% 4% at 60% 48%, rgba(200,200,200,0.22), transparent 75%),
      radial-gradient(ellipse 9% 5% at 82% 70%, rgba(200,200,200,0.25), transparent 75%),
      radial-gradient(ellipse 12% 5% at 12% 58%, rgba(180,180,180,0.20), transparent 75%),
      radial-gradient(ellipse 80% 70% at 50% 110%, rgba(70,70,70,0.6), transparent 75%),
      linear-gradient(180deg, #141414 0%, #1b1b1b 40%, #232323 100%);
  }
  .tech-heading { top: 225px; font-weight: 400; font-size: 23px; letter-spacing: 2px; }
  .tech-tagline { top: 262px; font-size: 15px; font-style: italic; letter-spacing: 1.4px; color: var(--text-soft); }
  .tech-text {
    top: 297px; left: 400px; width: 400px;
    font-size: 10.5px; line-height: 15px; letter-spacing: 0.7px; color: var(--text-soft);
  }
  .tech-text p + p { margin-top: 15px; }

  /* Quote: scattered brass casings tones */
  .quote { top: 2024px; height: 675px; }
  .quote .backdrop {
    background:
      linear-gradient(75deg, transparent 30%, rgba(120,70,30,0.18) 34%, transparent 38%),
      linear-gradient(160deg, transparent 55%, rgba(110,65,28,0.16) 59%, transparent 63%),
      radial-gradient(ellipse 16% 20% at 38% 30%, rgba(120,70,30,0.38), transparent 75%),
      radial-gradient(ellipse 14% 16% at 12% 55%, rgba(100,55,25,0.32), transparent 75%),
      radial-gradient(ellipse 18% 15% at 72% 75%, rgba(110,62,28,0.35), transparent 75%),
      radial-gradient(ellipse 14% 18% at 88% 35%, rgba(95,55,25,0.3), transparent 75%),
      radial-gradient(ellipse 16% 14% at 30% 85%, rgba(100,58,26,0.3), transparent 75%),
      linear-gradient(180deg, #171411 0%, #15120f 100%);
  }
  .quote-text { top: 290px; font-size: 31px; font-weight: 700; font-style: italic; letter-spacing: 3px; }
  .quote-author { top: 350px; font-size: 15px; font-weight: 700; font-style: italic; letter-spacing: 1.4px; }

  .footer-space { top: 2699px; height: 426px; background: var(--page-dark); }

  .scroll-mouse { position: absolute; left: 588px; width: 24px; height: 32px; }
</style>
</head>
<body>
<main class="page">

  <section class="section hero">
    <div class="backdrop" role="img" aria-label="Misty forest path with sunlight rays, in greyscale"></div>
    <div class="brand-name">Vlm Quarvex</div>
    <h1 class="content hero-title">Sustainable solutions to the defense industry</h1>
    <p class="content hero-intro">Welcome to Vlm Quarvex, the advanced Technology Company paving the way to the future. We are a team of like-minded and determined individuals, all sharing a vision for success. We believe that our sophisticated technology has the potential to become an industry sensation. Would you like to find out more? Our website will be updated on a regular basis.</p>
    <a class="cta" href="#">Get in touch</a>
    <svg class="scroll-mouse" style="top:628px" viewBox="0 0 24 32" aria-hidden="true">
      <path d="M11 0 A11 11 0 0 0 0 11 V13 H11 Z M13 0 A11 11 0 0 1 24 11 V13 H13 Z M0 15 H24 V21 A11 11 0 0 1 0 21 Z" fill="var(--mouse-grey)"/>
    </svg>
  </section>

  <section class="section who">
    <div class="backdrop" role="img" aria-label="Soldier with night vision helmet holding a rifle, darkened"></div>
    <h2 class="content section-heading who-heading">WHO WE ARE</h2>
    <p class="content who-text">Vlm Quarvex is a leading provider of cutting-edge technologies and services, offering scalable solutions for the defense and security industry of all sizes. Founded by a group of friends who started by scribbling their ideas on a bus ride in San Francisco. Today we are working on innovative solutions to disrupt the training industry with a sustainable solution.</p>
    <svg class="scroll-mouse" style="top:628px" viewBox="0 0 24 32" aria-hidden="true">
      <path d="M11 0 A11 11 0 0 0 0 11 V13 H11 Z M13 0 A11 11 0 0 1 24 11 V13 H13 Z M0 15 H24 V21 A11 11 0 0 1 0 21 Z" fill="var(--mouse-grey)"/>
    </svg>
  </section>

  <section class="section tech">
    <div class="backdrop" role="img" aria-label="Earth at night seen from orbit with city lights"></div>
    <h2 class="content section-heading tech-heading">OUR INNOVATIVE TECHNOLOGY</h2>
    <p class="content tech-tagline">The Possibilities Are Endless</p>
    <div class="content tech-text">
      <p>At Vlm Quarvex, our comprehensive technological solutions help the industry to become more sustainable and efficient with the spendings. We will balance qualitative training experience for soldiers and security forces with real life experiences and a real life feel.</p>
      <p>Our platform will have a wide range of features created with the aim to help the industry become more aware of their environmental footprint. In order to empower our users to do better, Vlm Quarvex is continually building upon its technology, so stay in touch to learn about upgrades and other changes. For a free demo, feel free to contact us.</p>
    </div>
    <svg class="scroll-mouse" style="top:627px" viewBox="0 0 24 32" aria-hidden="true">
      <path d="M11 0 A11 11 0 0 0 0 11 V13 H11 Z M13 0 A11 11 0 0 1 24 11 V13 H13 Z M0 15 H24 V21 A11 11 0 0 1 0 21 Z" fill="var(--mouse-grey)"/>
    </svg>
  </section>

  <section class="section quote">
    <div class="backdrop" role="img" aria-label="Scattered brass bullet casings, darkened"></div>
    <blockquote class="content quote-text">"The secret of getting ahead is getting started"</blockquote>
    <p class="content quote-author">Elias Brandt</p>
    <svg class="scroll-mouse" style="top:628px" viewBox="0 0 24 32" aria-hidden="true">
      <path d="M11 0 A11 11 0 0 0 0 11 V13 H11 Z M13 0 A11 11 0 0 1 24 11 V13 H13 Z M0 15 H24 V21 A11 11 0 0 1 0 21 Z" fill="var(--mouse-grey)"/>
    </svg>
  </section>

  <section class="section footer-space" aria-hidden="true"></section>

</main>
</body>
</html>
```